Full redesign of dairy products including Yogurts and milk products

We have been selling milk and yogurts over the past 15 years, we are now expanding into a wider range of dairy products to include flavoured milk and a variety of soft cheeses such as cottage cheese etc. It is now the perfect time to redesign our existing product range to give a fresh and new look to our products. Have a look at our website https://rtvale.co.uk/ for further details. We are rebranding as NUVELKA, I have attached a identify pack to give you a feel of the the design, this is a fresh and bright design that will reflect the fresh and tasteful products we produce. The current milk label cut out is unique to us and I would like to continue using this shape which I have attached, the other labels should be done using regular rectangular rounded edge labels. The following designs are required;
1 x Universal lid (71.5mm) design for all below 120ml Yogurts
-11 x 120 ml Yogurt pot designs
Strawberry
Strawberry Banana
Peach & Apricot
Cherry
Toffee
Vanilla
Natural
Orange
Forest Fruits
Pineapple
Mango
1 x Universal lid (95.5mm)for below yogurts (can be identical to the 120ml Lid)
-4 x 450ml Yogurt Pots
Strawberry
Natural
Toffee
Mango
-1 x Universal (95.5mm) LID for 150ml Greek Yogurt
-4 x Designs for 150ml Greek yogurt POT
Strawberry
Natural
Vanilla
Mango

3 x Flavoured milk labels 2 sizes 250ml & 1lt
Biscotti
Chocolate
Strawberry

Cottage Cheese Lid & Pot 250g

1 x Quark universal Lid (95.5mm)
4 x Quark 250g pots
Natural
Strawberry
Peach & Apricot
Mango

```html
<!DOCTYPE html>
<html lang="en">
<head>
<meta charset="utf-8">
<title>NUVELKA Strawberry Yogurt 450 Gr – Pot Label</title>
<link rel="stylesheet" href="https://fonts.googleapis.com/css2?family=Fredoka:wght@500;600;700&family=Oleo+Script:wght@700&display=swap">
<style>
  :root{
    --page:#ffffff;
    --blue-deep:#1a8fe0;
    --blue-mid:#2aa6ec;
    --blue-light:#5cc8f5;
    --label-white:#fbfdfe;
    --splash-grey:#e9edf0;
    --brand-green:#3fae3c;
    --flavour-red:#c8141e;
    --type-navy:#1b1f5e;
    --berry-red:#d2302e;
    --berry-dark:#a81d1f;
  }
  *{margin:0;padding:0;box-sizing:border-box}
  html,body{width:1200px;height:1200px;overflow:hidden;background:var(--page)}
  .canvas{position:relative;width:1200px;height:1200px}
  .label{position:absolute;left:220px;top:160px;width:760px;height:880px;border-radius:28px;overflow:hidden;background:var(--label-white)}
  .label-art{position:absolute;inset:0;width:100%;height:100%}
  .brand{position:absolute;left:0;right:0;top:212px;display:flex;justify-content:center;align-items:center;gap:16px}
  .brand-dot{width:34px;height:34px;border-radius:50%;background:var(--brand-green)}
  .brand-name{font-family:"Fredoka",sans-serif;font-weight:700;font-size:64px;letter-spacing:2px;color:var(--brand-green);line-height:1}
  .flavour{position:absolute;left:240px;top:320px;font-family:"Oleo Script",cursive;font-weight:700;font-size:92px;color:var(--flavour-red);line-height:1}
  .product{position:absolute;left:318px;top:438px;font-family:"Fredoka",sans-serif;font-weight:600;font-size:118px;color:var(--type-navy);line-height:1}
  .weight{position:absolute;right:110px;bottom:98px;font-family:"Fredoka",sans-serif;font-weight:600;font-size:52px;color:#ffffff;line-height:1}
</style>
</head>
<body>
<div class="canvas">
  <div class="label">
    <svg class="label-art" viewBox="0 0 760 880" xmlns="http://www.w3.org/2000/svg">
      <defs>
        <linearGradient id="bandTop" x1="0" y1="0" x2="0" y2="1">
          <stop offset="0" stop-color="#1a8fe0"/>
          <stop offset="1" stop-color="#5cc8f5"/>
        </linearGradient>
        <linearGradient id="bandBottom" x1="0" y1="0" x2="0" y2="1">
          <stop offset="0" stop-color="#5cc8f5"/>
          <stop offset="1" stop-color="#1a8fe0"/>
        </linearGradient>
        <radialGradient id="splash" cx="0.55" cy="0.5" r="0.6">
          <stop offset="0" stop-color="#ffffff"/>
          <stop offset="1" stop-color="#e3e8ec"/>
        </radialGradient>
        <radialGradient id="berry" cx="0.45" cy="0.4" r="0.6">
          <stop offset="0" stop-color="#e0423c"/>
          <stop offset="1" stop-color="#a81d1f"/>
        </radialGradient>
      </defs>
      <rect class="band-top" x="0" y="0" width="760" height="200" fill="url(#bandTop)"/>
      <path class="band-top-wave" d="M0 160 C200 110 520 110 760 190 L760 240 C520 170 220 170 0 230 Z" fill="#2aa6ec" opacity="0.55"/>
      <path class="band-bottom" d="M0 720 C180 690 480 760 760 700 L760 880 L0 880 Z" fill="url(#bandBottom)"/>
      <path class="band-bottom-wave" d="M0 770 C220 740 500 800 760 760 L760 880 L0 880 Z" fill="#1a8fe0"/>
      <g role="img" aria-label="Photograph of a creamy white yogurt splash">
        <ellipse cx="430" cy="440" rx="340" ry="300" fill="url(#splash)"/>
      </g>
      <g role="img" aria-label="Photograph of a ripe strawberry with green leaves dipping into the yogurt splash">
        <ellipse cx="205" cy="545" rx="120" ry="135" fill="url(#berry)"/>
      </g>
    </svg>
    <div class="brand"><span class="brand-dot"></span><span class="brand-name">NUVELKA</span></div>
    <div class="flavour">Strawberry</div>
    <div class="product">Yogurt</div>
    <div class="weight">450 Gr</div>
  </div>
</div>
</body>
</html>
```